Quillbrook Health needs a new services brochure

We need a new brochure that highlights the services that we offer at our clinic. We are a multidisciplinary health clinic that focuses on injury rehabilitation and pain management. We are looking for a brochure that will highlight our primary services to our clientele and inform potential clients of what we can offer. We pride ourselves on our quality of care and our advanced treatment techniques.
Target Market(s)
young families, athletes, people interested in their health.
Industry/Entity Type
Health And Wellness
Colors
Designer to choose colors to be used in the design.
Requirements
Must have
- We would love our new brochure to be a tri-fold that has 6 pages. We would like it to have brief information about our featured services:
- - Chiropractic
- - Massage Therapy
- - Manual Osteopathic Therapy
- - Acupuncture
- - Laser Therapy
- - Radial Shockwave Therapy
- We would also like this brochure to include a brief price list and direct billing info, About Us section & Contact information.
Nice to have
- If there is space to list that we also offer other services such as : Tissue Unwind Method, Hot Stone Massage, Cupping Technique, Pembrill Method, and Kinesiology Taping that would be great. We would like to use images similar to those that are on our website (we have hi-res of all images on the website) www.quillbrookhealth.ca and colours that would fit with our logo.

```html
<!DOCTYPE html>
<html lang="en">
<head>
<meta charset="utf-8">
<title>Quillbrook Health – Services Brochure</title>
<link href="https://fonts.googleapis.com/css2?family=Open+Sans:wght@400;600;700;800&display=swap" rel="stylesheet">
<style>
:root{
  --blue:#1b5ea8;
  --blue-dark:#164e8e;
  --grey:#8f9296;
  --paper:#ffffff;
  --mist:#eef2f6;
  --bg:#dfe6ee;
  --ink:#1d2430;
}
*{box-sizing:border-box;margin:0;padding:0}
html,body{width:931px;height:1200px;overflow:hidden}
body{background:var(--bg);font-family:"Open Sans",sans-serif;color:var(--ink);position:relative}
.sheet{position:absolute;left:20px;width:891px;height:560px;background:var(--paper);overflow:hidden;box-shadow:0 3px 10px rgba(0,0,0,.18)}
.sheet--outside{top:25px}
.sheet--inside{top:615px}
.panel{position:absolute;top:0;width:297px;height:560px}
.p1{left:0}.p2{left:297px}.p3{left:594px}
.art{position:absolute;left:0;top:0}
.blue{background:var(--blue);color:#fff}
h2{font-weight:800;line-height:1.1}
p,li{font-size:7.4px;line-height:1.38}
ul{list-style:none}
li::before{content:"\2022";margin-right:4px}

/* direct bill */
.direct{position:absolute;left:20px;right:20px;top:196px}
.direct h2{font-size:25px;margin-bottom:8px}
.direct p{margin-bottom:6px;text-align:justify}
.direct ul{margin:2px 0 8px 8px}
.direct li{font-size:7.8px;line-height:1.3}

/* about */
.about{position:absolute;left:22px;right:22px;top:34px;text-align:center}
.about h2{font-size:24px;margin-bottom:8px}
.about p{margin-bottom:7px}
.seal{position:absolute;left:76px;top:250px;width:150px;height:150px;border-radius:50%;background:#fff;display:flex;align-items:center;justify-content:center;gap:5px}
.brand{font-weight:700;color:var(--blue);font-size:14px;white-space:nowrap}
.brand-dot{width:10px;height:10px;border-radius:50%;background:var(--blue);flex:none}
.contact{position:absolute;left:24px;top:430px;font-size:8px;line-height:1.45}
.contact .phone{font-size:15px;font-weight:700;margin-bottom:4px}
.webband{position:absolute;left:0;right:0;bottom:0;height:46px;background:#fff;color:var(--blue);font-weight:700;font-size:12px;display:flex;align-items:center;padding-left:24px}

/* cover */
.cover-logo{position:absolute;left:40px;top:30px;display:flex;align-items:center;gap:6px}
.cover-logo .brand{font-size:19px}
.cover-logo .brand-dot{width:14px;height:14px}
.tagband{position:absolute;left:62px;right:0;top:86px;height:40px;background:var(--grey);color:#fff;font-weight:800;font-size:30px;display:flex;align-items:center;padding-left:14px;letter-spacing:.5px}
.tagline{position:absolute;left:110px;top:128px;font-weight:700;font-size:22px;color:var(--blue)}

/* inside services */
.services{position:absolute;top:118px;width:270px}
.col-a{left:22px}
.col-b{left:318px;top:112px;width:260px}
.services h3{color:var(--blue);font-weight:800;font-size:14px;line-height:1.15;margin-top:5px}
.services h4{font-size:8px;font-weight:700;margin:1px 0 1px}
.services li{font-size:7.4px;line-height:1.24;margin-left:6px}

/* prices */
.prices{padding:22px 24px 0 24px}
.prices h2{font-size:23px;text-align:center}
.prices .gst{font-size:7.4px;text-align:center;font-weight:700;margin-top:2px}
.prices .gst span{display:block;font-weight:400}
.prices h3{font-size:9.5px;font-weight:700;margin:9px 0 2px}
.rate{display:grid;grid-template-columns:1fr 44px 44px;font-size:7.4px;line-height:1.3}
.rate.two{grid-template-columns:1fr 60px}
.rate .hd{font-weight:700}
.note{font-size:7.4px;line-height:1.3;margin-top:2px}
</style>
</head>
<body>

<section class="sheet sheet--outside">
  <div class="panel p1 blue">
    <svg class="art" width="297" height="200" viewBox="0 0 297 200">
      <defs>
        <linearGradient id="massageTone" x1="0" y1="0" x2="1" y2="1">
          <stop offset="0" stop-color="#c9a48c"/><stop offset="1" stop-color="#5c4a42"/>
        </linearGradient>
      </defs>
      <path d="M0 0 H262 Q250 150 0 190 Z" fill="#fff"/>
      <path d="M0 0 H252 Q240 140 0 180 Z" fill="url(#massageTone)" role="img" aria-label="Therapist's hands massaging a client's shoulder"/>
    </svg>
    <div class="direct">
      <h2>We Direct Bill</h2>
      <p>We are happy to offer direct billing to extended healthcare plans which allow direct billing and online claim submissions from providers.</p>
      <p>As all insurance companies and plans are different, we recommend asking your plan provider directly if they allow online direct billing on your specific plan. Unfortunately at this time, insurance companies do not allow an option for direct billing for Manual Osteopathy, except in the case of Greenleaf and Prairie Shield. Most insurance plans do allow patients to submit manual osteopathy claims online and if you are set up for direct deposit, most plans will deposit claim payments within 48 hours.</p>
      <p>The following insurance companies typically allow online direct billing:</p>
      <ul>
        <li>Prairie Shield Benefits</li><li>Northgate Mutual</li><li>Cobalt Health Plans</li><li>Hearthline Insurance</li><li>Westvale Life</li><li>Greenleaf Benefits Canada</li><li>Arbor Financial Group</li><li>Kestrel Insurance</li><li>Kestrel Group</li><li>Maplecrest Life</li><li>Summit Benefit</li><li>Lakeshore Life</li><li>Sunvale</li>
      </ul>
      <p>Occasionally some insurance companies will conduct random audits on claims or send claims for further processing. <b>In these instances, we are unable to direct bill for that individual claim.</b> The insurance company will send payment directly to you once the claim has been processed.</p>
    </div>
  </div>

  <div class="panel p2 blue">
    <div class="about">
      <h2>About Us</h2>
      <p>Quillbrook Health is a Chiropractic, Massage Therapy, Manual Osteopathy, Acupuncture, Shockwave and Laser Therapy clinic in NW Calgary. We bring a comprehensive approach to pain relief and injury recovery to help you get back to enjoying a healthy, active life. Our mission is to provide the best rehabilitative solutions to our patients so they can feel better in the most efficient and comfortable way possible.</p>
      <p>Quillbrook Health is owned and operated by Dan and Mara Ellison, long time residents of NW Calgary. Most of our team members both live and work in NW Calgary too. We take great care and pride in helping our patients, many of whom are quite literally our neighbours, move better, feel better and live better. Our approach is patient-focused and evidence informed (backed by credible scientific research). We are located just north of Ridgeway Trail in Fernmoor, one of NW Calgary's largest communities.</p>
    </div>
    <div class="seal"><span class="brand-dot"></span><span class="brand">Quillbrook Health</span></div>
    <div class="contact">
      <div class="phone">(403) 555-0182</div>
      Harlow Crossing Centre<br>4410 - 1875 Fernmoor Pkwy NW<br>Calgary, AB T3P 2K7
    </div>
    <div class="webband">www.quillbrookhealth.ca</div>
  </div>

  <div class="panel p3">
    <svg class="art" width="297" height="560" viewBox="0 0 297 560">
      <defs>
        <linearGradient id="runnerTone" x1="0" y1="0" x2="0.6" y2="1">
          <stop offset="0" stop-color="#e9a04a"/><stop offset=".4" stop-color="#6f9a4a"/><stop offset=".6" stop-color="#a9573a"/><stop offset="1" stop-color="#8a4a33"/>
        </linearGradient>
      </defs>
      <path d="M297 170 V560 H0 V470 Q-10 290 120 205 Q200 160 297 170 Z" fill="var(--blue)"/>
      <path d="M297 182 V560 H12 V470 Q5 300 130 215 Q205 172 297 182 Z" fill="url(#runnerTone)" role="img" aria-label="Runner sprinting on an outdoor track at sunset"/>
    </svg>
    <div class="cover-logo"><span class="brand-dot"></span><span class="brand">Quillbrook Health</span></div>
    <div class="tagband">LIVE LIFE</div>
    <div class="tagline">pain free</div>
  </div>
</section>

<section class="sheet sheet--inside">
  <svg class="art" width="594" height="560" viewBox="0 0 594 560">
    <defs>
      <linearGradient id="mistTone" x1="0" y1="0" x2="1" y2="1">
        <stop offset="0" stop-color="#f3f5f8"/><stop offset="1" stop-color="#dde3ea"/>
      </linearGradient>
      <linearGradient id="backTone" x1="0" y1="0" x2="1" y2="0">
        <stop offset="0" stop-color="#3a3440"/><stop offset=".6" stop-color="#d8b8a2"/><stop offset="1" stop-color="#e8e8ea"/>
      </linearGradient>
      <linearGradient id="kneeTone" x1="0" y1="0" x2="1" y2="0">
        <stop offset="0" stop-color="#2a2a2e"/><stop offset=".5" stop-color="#d9a98d"/><stop offset="1" stop-color="#f0ece8"/>
      </linearGradient>
    </defs>
    <rect width="594" height="560" fill="url(#mistTone)" role="img" aria-label="Faint background photo of a treatment session"/>
    <path d="M200 0 H480 Q460 105 330 112 Q230 112 200 0 Z" fill="var(--blue)"/>
    <path d="M208 0 H470 Q452 98 330 104 Q236 104 208 0 Z" fill="url(#backTone)" role="img" aria-label="Chiropractor adjusting a patient's upper back"/>
    <path d="M190 560 Q215 484 330 482 Q435 484 462 560 Z" fill="var(--blue)"/>
    <path d="M200 560 Q223 491 330 489 Q427 491 454 560 Z" fill="url(#kneeTone)" role="img" aria-label="Therapist examining an athlete's knee"/>
  </svg>

  <div class="services col-a">
    <h3>Calgary Chiropractor</h3>
    <h4>We can help you:</h4>
    <ul>
      <li>Find relief from pain</li><li>Find relief from headaches</li><li>Improve movement of your back, neck and shoulders</li><li>Improve posture</li><li>Correct foot or gait problems</li><li>Correct or improve TMJ (jaw) dysfunction</li><li>Improve athletic performance</li><li>Increase energy level</li>
    </ul>
    <h3>Calgary Massage Therapy</h3>
    <ul>
      <li>Eliminate pain</li><li>Increase range of motion</li><li>Relax tight muscles</li><li>Decrease headaches</li><li>Correct or improve TMJ (jaw) dysfunction</li><li>Decrease anxiety</li><li>Recover from injuries faster</li><li>Improve posture</li><li>Assist GI function</li>
    </ul>
    <h3>Calgary Manual Osteopathy</h3>
    <h4>We can help you find relief from:</h4>
    <ul>
      <li>Pain</li><li>Joint stiffness</li><li>Sprains</li><li>Plantar Fasciitis</li><li>Rotator Cuff injuries</li><li>Whiplash/ MVA injuries</li><li>Back injuries/ pain</li><li>Fibromyalgia</li>
    </ul>
  </div>

  <div class="services col-b">
    <ul>
      <li>Headaches</li><li>Muscle injuries</li><li>Ligament tears/ injuries</li><li>Jaw pain/ TMJ disfunction</li>
    </ul>
    <h3>Calgary Acupuncture</h3>
    <h4>We can help you:</h4>
    <ul>
      <li>Find relief from pain</li><li>Increase energy levels</li><li>Improve overall mood</li><li>Improve bodily functions</li><li>Achieve body homeostasis (internal balance)</li>
    </ul>
    <h3>Calgary Shockwave Therapy</h3>
    <h4>We can help you with:</h4>
    <ul>
      <li>Plantar Fasciitis and Heel Spurs</li><li>Patella Tendonitis (runners knee)</li><li>Tennis/ Golfer's Elbow</li><li>Chronic Shoulder Pain</li><li>Neck Pain</li><li>Shin Splints</li><li>Chronic Hip Pain</li><li>Decreased Range of Motion</li>
    </ul>
    <h3>Calgary Laser Therapy</h3>
    <h4>We can help you with:</h4>
    <ul>
      <li>Post Surgical Incisions</li><li>Wound Healing</li><li>Sprains and Strains</li><li>Arthritis</li><li>Inflammation</li><li>Chronic Pain</li><li>Skin Conditions (psoriasis, cold sores, etc.)</li><li>Shin Splints</li><li>Tendonitis</li>
    </ul>
  </div>

  <div class="panel p3 blue prices">
    <h2>Prices</h2>
    <p class="gst">GST will be added to all applicable services:<span>Massage Therapy, Shockwave, Laser</span></p>

    <h3>Chiropractic</h3>
    <div class="rate">
      <span></span><span class="hd">Initial</span><span class="hd">Subsequent</span>
      <span>Pediatrics 0-5 yr old</span><span>$115</span><span>$55</span>
      <span>Student ( 6+yrs, full time)</span><span>$115</span><span>$55</span>
      <span>Adult</span><span>$125</span><span>$65</span>
      <span>Senior 65+ yrs</span><span>$115</span><span>$55</span>
      <span>Chiropractic and laser treatment</span><span></span><span>$95</span>
      <span>Chiropractic and shockwave therapy</span><span></span><span>$95</span>
    </div>

    <h3>Massage Therapy</h3>
    <div class="rate two">
      <span>30 Minute</span><span>$50</span>
      <span>45 Minute</span><span>$75</span>
      <span>60 Minutes</span><span>$90</span>
      <span>90 Minutes</span><span>$130</span>
      <span>Infant Massage Instruction</span><span>$50</span>
      <span>Hot Stone Addition</span><span>+$20 to regular treatment price</span>
    </div>

    <h3>Manual Osteopathic Therapy</h3>
    <div class="rate two">
      <span>Initial Assessment and Treatment</span><span>$150</span>
      <span>Subsequent Treatment</span><span>$120</span>
    </div>
    <p class="note">Unfortunately at this time, insurance companies do not allow an option for direct billing for Manual Osteopathy, except in the case of Greenleaf and Prairie Shield.</p>

    <h3>Acupuncture</h3>
    <div class="rate two">
      <span>Initial Assessment and Treatment</span><span>$120</span>
      <span>Subsequent Treatment</span><span>$85</span>
    </div>

    <h3>Shockwave Therapy</h3>
    <div class="rate two">
      <span>Initial Assessment and Treatment</span><span>$90</span>
      <span>Subsequent Treatments</span><span>$75</span>
    </div>

    <h3>Laser Therapy</h3>
    <div class="rate two">
      <span>Initial Assessment and Treatment</span><span>$90</span>
      <span>Subsequent Treatments</span><span>$50</span>
    </div>
  </div>
</section>

</body>
</html>
```